Flyer for a marketing

We are a holistic mental health facility in need of a flyer to help promote our services and encourage more people to seek care. See the attachment to tell you more. We prefer warm green colors or rich blue. Thank you.

```html
<!DOCTYPE html>
<html lang="en">
<head>
<meta charset="utf-8">
<title>The Care You Deserve – Evergreen Mind Health and Wellness</title>
<link href="https://fonts.googleapis.com/css2?family=DM+Serif+Display&family=Montserrat:ital,wght@0,400;0,500;0,600;0,700;0,800;1,500&display=swap" rel="stylesheet">
<style>
  :root {
    --green: #3b8a3e;
    --green-dark: #2a6b2f;
    --green-soft: #e6f0e3;
    --navy: #1d2b4c;
    --navy-deep: #15213d;
    --ink: #2c3444;
    --muted: #5d6675;
    --white: #ffffff;
    --photo-a: #c9d6cc;
    --photo-b: #8fa7a0;
  }
  * { box-sizing: border-box; margin: 0; padding: 0; }
  html, body { width: 784px; height: 1200px; overflow: hidden; background: var(--white); }
  body { font-family: "Montserrat", Arial, sans-serif; color: var(--ink); }
  .flyer { position: relative; width: 784px; height: 1200px; background: var(--white); }

  .brand { position: absolute; left: 40px; top: 40px; display: flex; align-items: center; gap: 12px; }
  .brand-mark { width: 46px; height: 46px; border-radius: 50%; background: var(--green); }
  .brand-name { font-weight: 700; font-size: 15px; line-height: 1.2; color: var(--green-dark); }

  .headline { position: absolute; left: 40px; top: 150px; width: 380px; }
  .headline-top { font-weight: 800; font-size: 46px; color: var(--navy); letter-spacing: .5px; line-height: 1; }
  .headline-big { font-family: "DM Serif Display", Georgia, serif; font-size: 92px; color: var(--green); line-height: .95; letter-spacing: 1px; }
  .subhead { margin-top: 18px; font-weight: 700; font-size: 24px; line-height: 1.2; color: var(--navy); }
  .tagline { margin-top: 6px; font-size: 19px; font-weight: 500; color: var(--ink); line-height: 1.3; }

  .hero-frame { position: absolute; left: 420px; top: 40px; width: 324px; height: 420px;
    border: 12px solid var(--green); border-radius: 170px 0 0 0; overflow: hidden; background: var(--green-soft); }
  .hero-photo { width: 100%; height: 100%; background: linear-gradient(160deg, var(--photo-a), var(--photo-b)); }
  .hero-accent { position: absolute; left: 404px; top: 380px; width: 18px; height: 100px; background: var(--navy); }

  .intake { position: absolute; left: 40px; top: 480px; width: 350px; height: 290px; background: var(--navy); padding: 22px; color: var(--white); }
  .intake-row { display: flex; gap: 16px; align-items: flex-start; }
  .intake-label { font-weight: 800; font-size: 22px; line-height: 1.1; }
  .intake-label .accent { color: #8fd08f; }
  .intake-divider { width: 2px; height: 52px; background: rgba(255,255,255,.5); }
  .intake-note { margin-top: 10px; font-size: 12px; line-height: 1.4; color: #d6dcea; width: 180px; }
  .intake-photo { position: absolute; right: 22px; top: 96px; width: 130px; height: 120px; border-radius: 8px;
    background: linear-gradient(150deg, #b8c8d8, #7d93ad); }
  .appointment { position: absolute; left: 22px; right: 22px; bottom: 20px; height: 48px; background: var(--green);
    color: var(--white); font-weight: 800; font-size: 22px; letter-spacing: 1.5px; display: flex; align-items: center; justify-content: center; gap: 10px; }

  .why { position: absolute; left: 420px; top: 490px; width: 324px; }
  .why-title { font-family: "DM Serif Display", Georgia, serif; font-size: 30px; color: var(--navy); }
  .why-list { list-style: none; margin-top: 12px; }
  .why-list li { display: flex; gap: 10px; font-size: 14px; line-height: 1.35; margin-bottom: 11px; color: var(--ink); }
  .why-list svg { flex: none; margin-top: 1px; }

  .services-title { position: absolute; left: 40px; right: 40px; top: 800px; display: flex; align-items: center; gap: 16px;
    font-family: "DM Serif Display", Georgia, serif; font-size: 26px; color: var(--navy); }
  .services-title::before, .services-title::after { content: ""; flex: 1; height: 2px; background: var(--green); }
  .services { position: absolute; left: 40px; right: 40px; top: 852px; display: flex; gap: 12px; }
  .service { flex: 1; height: 170px; background: var(--green); color: var(--white); border-radius: 10px 10px 0 0;
    display: flex; flex-direction: column; align-items: center; padding: 20px 8px 0; text-align: center; }
  .service-icon { width: 56px; height: 56px; border-radius: 50%; background: var(--white); display: flex; align-items: center; justify-content: center; }
  .service-name { margin-top: 14px; font-weight: 700; font-size: 13px; line-height: 1.3; }

  .contact { position: absolute; left: 40px; right: 40px; top: 1060px; display: flex; justify-content: space-between; font-size: 14px; color: var(--ink); }
  .contact-col { display: flex; flex-direction: column; gap: 10px; }
  .contact-item { display: flex; align-items: center; gap: 9px; }
  .footer-band { position: absolute; left: 0; right: 0; bottom: 0; height: 26px; background: var(--green); }
</style>
</head>
<body>
<main class="flyer">
  <div class="brand">
    <div class="brand-mark"></div>
    <div class="brand-name">Evergreen Mind<br>Health and<br>Wellness</div>
  </div>

  <section class="headline">
    <h1><span class="headline-top">THE CARE YOU</span><br><span class="headline-big">DESERVE</span></h1>
    <p class="subhead">Evergreen Mind Health and Wellness</p>
    <p class="tagline">where deserving patients meet compassionate providers.</p>
  </section>

  <div class="hero-accent"></div>
  <div class="hero-frame">
    <div class="hero-photo" role="img" aria-label="Photo of a caregiver kindly supporting an older patient at home"></div>
  </div>

  <section class="intake">
    <div class="intake-row">
      <div class="intake-label"><span class="accent">ACCEPTING</span><br>NEW PATIENTS</div>
      <div class="intake-divider"></div>
      <div class="intake-label"><span class="accent">NO</span><br>WAITING</div>
    </div>
    <p class="intake-note">Book your first visit today and meet a caring provider without a long wait.</p>
    <div class="intake-photo" role="img" aria-label="Photo of a smiling patient talking with a provider"></div>
    <div class="appointment">
      <svg width="22" height="22" viewBox="0 0 24 24" fill="none" stroke="#fff" stroke-width="2"><rect x="3" y="5" width="18" height="16" rx="2"/><path d="M3 10h18M8 3v4M16 3v4"/></svg>
      APPOINTMENT
    </div>
  </section>

  <section class="why">
    <h2 class="why-title">WHY CHOOSE US!</h2>
    <ul class="why-list">
      <li><svg width="18" height="18" viewBox="0 0 20 20"><circle cx="10" cy="10" r="9" fill="none" stroke="#3b8a3e" stroke-width="2"/><path d="M6 10l3 3 5-6" fill="none" stroke="#3b8a3e" stroke-width="2"/></svg>We are an integrative holistic psychiatric center.</li>
      <li><svg width="18" height="18" viewBox="0 0 20 20"><circle cx="10" cy="10" r="9" fill="none" stroke="#3b8a3e" stroke-width="2"/><path d="M6 10l3 3 5-6" fill="none" stroke="#3b8a3e" stroke-width="2"/></svg>Our mission is to provide high-quality, compassionate care.</li>
      <li><svg width="18" height="18" viewBox="0 0 20 20"><circle cx="10" cy="10" r="9" fill="none" stroke="#3b8a3e" stroke-width="2"/><path d="M6 10l3 3 5-6" fill="none" stroke="#3b8a3e" stroke-width="2"/></svg>We listen, care, and empower you to live better.</li>
      <li><svg width="18" height="18" viewBox="0 0 20 20"><circle cx="10" cy="10" r="9" fill="none" stroke="#3b8a3e" stroke-width="2"/><path d="M6 10l3 3 5-6" fill="none" stroke="#3b8a3e" stroke-width="2"/></svg>We provide psychiatric services including medication management and psychotherapy.</li>
      <li><svg width="18" height="18" viewBox="0 0 20 20"><circle cx="10" cy="10" r="9" fill="none" stroke="#3b8a3e" stroke-width="2"/><path d="M6 10l3 3 5-6" fill="none" stroke="#3b8a3e" stroke-width="2"/></svg>We treat both children and adults.</li>
      <li><svg width="18" height="18" viewBox="0 0 20 20"><circle cx="10" cy="10" r="9" fill="none" stroke="#3b8a3e" stroke-width="2"/><path d="M6 10l3 3 5-6" fill="none" stroke="#3b8a3e" stroke-width="2"/></svg>We accept major insurances.</li>
    </ul>
  </section>

  <h2 class="services-title">OUR SERVICES</h2>
  <section class="services">
    <div class="service">
      <div class="service-icon"><svg width="28" height="28" viewBox="0 0 24 24" fill="none" stroke="#3b8a3e" stroke-width="2"><rect x="5" y="4" width="14" height="18" rx="2"/><path d="M9 3h6v3H9zM8 11h8M8 15h6"/></svg></div>
      <div class="service-name">Comprehensive Psychiatric Evaluations</div>
    </div>
    <div class="service">
      <div class="service-icon"><svg width="28" height="28" viewBox="0 0 24 24" fill="none" stroke="#3b8a3e" stroke-width="2"><rect x="3" y="8" width="18" height="8" rx="4" transform="rotate(-40 12 12)"/><path d="M9.5 9l5 6"/></svg></div>
      <div class="service-name">Psychiatric Medication</div>
    </div>
    <div class="service">
      <div class="service-icon"><svg width="28" height="28" viewBox="0 0 24 24" fill="none" stroke="#3b8a3e" stroke-width="2"><rect x="3" y="5" width="18" height="16" rx="2"/><path d="M3 10h18M8 3v4M16 3v4M8 15l2 2 4-4"/></svg></div>
      <div class="service-name">Medication Management Follow-ups</div>
    </div>
    <div class="service">
      <div class="service-icon"><svg width="28" height="28" viewBox="0 0 24 24" fill="none" stroke="#3b8a3e" stroke-width="2"><path d="M12 20s-7-4.5-7-10a4 4 0 0 1 7-2.5A4 4 0 0 1 19 10c0 5.5-7 10-7 10z"/></svg></div>
      <div class="service-name">Integrated Treatment Planning</div>
    </div>
    <div class="service">
      <div class="service-icon"><svg width="28" height="28" viewBox="0 0 24 24" fill="none" stroke="#3b8a3e" stroke-width="2"><path d="M4 5h16v11H9l-5 4z"/><path d="M8 9h8M8 12h5"/></svg></div>
      <div class="service-name">Intensive Focused Psychotherapy</div>
    </div>
  </section>

  <footer class="contact">
    <div class="contact-col">
      <div class="contact-item"><svg width="18" height="18" viewBox="0 0 24 24" fill="#3b8a3e"><path d="M12 2a7 7 0 0 0-7 7c0 5 7 13 7 13s7-8 7-13a7 7 0 0 0-7-7zm0 9.5A2.5 2.5 0 1 1 12 6.5a2.5 2.5 0 0 1 0 5z"/></svg>418 Maple Grove Road, Suite 120, Fairview, CA 90210</div>
      <div class="contact-item"><svg width="18" height="18" viewBox="0 0 24 24" fill="#3b8a3e"><path d="M6.6 10.8a15 15 0 0 0 6.6 6.6l2.2-2.2a1 1 0 0 1 1-.25 11 11 0 0 0 3.6.6 1 1 0 0 1 1 1V20a1 1 0 0 1-1 1A17 17 0 0 1 3 4a1 1 0 0 1 1-1h3.5a1 1 0 0 1 1 1 11 11 0 0 0 .6 3.6 1 1 0 0 1-.25 1z"/></svg>(555) 214-3080 &nbsp;|&nbsp; (555) 214-3095</div>
    </div>
    <div class="contact-col">
      <div class="contact-item"><svg width="18" height="18" viewBox="0 0 24 24" fill="none" stroke="#3b8a3e" stroke-width="2"><rect x="3" y="5" width="18" height="14" rx="2"/><path d="M3 7l9 6 9-6"/></svg>care@evergreenmindhealth.com</div>
      <div class="contact-item"><svg width="18" height="18" viewBox="0 0 24 24" fill="none" stroke="#3b8a3e" stroke-width="2"><circle cx="12" cy="12" r="9"/><path d="M3 12h18M12 3c3 3 3 15 0 18M12 3c-3 3-3 15 0 18"/></svg>www.evergreenmindhealth.com</div>
    </div>
  </footer>
  <div class="footer-band"></div>
</main>
</body>
</html>
```